Audit/Compliance company needs Business Card Template

We are after a Business Card Template that we can modify internally to update details as people change positions.
We are an Australian based company specalising in Auditing and Quality/OHS systems development. - See www.kelvaranorth.com.au for more information
We would like the desings to be based around our logo and colours assocaited with it (attached for your information) however we are very open as to how the cards are designed.
We are looking for something quite edgy and mordern but it must have a professional/compliance feel to it (if possible).
The main details we would like to include within the card template are:
Name
Position Title
Postal Address
Phone Number
Mobile Number
Email Address
Website
The cards will be printed through tally press on Glossy paper so it should reflect the requirements below
Full Bleed Size (starting document size)
90 x 52 mm
1062 x 615 pixels
Document Trim Size (final size after being cut)
87 x 49 mm
1028 x 579 pixels
Resolution
300 DPI

```html
<!DOCTYPE html>
<html lang="en">
<head>
<meta charset="utf-8">
<title>Kelvara North – Business Card</title>
<link rel="stylesheet" href="https://fonts.googleapis.com/css2?family=Didact+Gothic&family=Cabin:wght@400&display=swap">
<style>
  :root {
    --navy: #0f172c;
    --sky: #14b2e4;
    --orange: #f0821e;
    --panel: #eff0f2;
    --back: #f4f4f4;
    --ink: #4a4a4a;
    --page: #ffffff;
  }
  * { margin: 0; padding: 0; box-sizing: border-box; }
  html, body {
    width: 1076px; height: 1200px; overflow: hidden;
    background: var(--page);
  }
  .card { position: absolute; }

  .card-front {
    left: 116px; top: 76px; width: 886px; height: 512px;
    background: linear-gradient(to bottom, var(--navy) 0, var(--navy) 462px, var(--sky) 480px, var(--sky) 100%);
  }
  .brand-panel {
    position: absolute; left: 0; top: 181px; width: 479px; height: 150px;
    background: linear-gradient(to right, #e9eaec, var(--panel) 50%, #f6f6f7);
    border-radius: 0 34px 34px 0;
    display: flex; align-items: center; padding-left: 40px; gap: 26px;
  }
  .brand-mark { width: 64px; height: 64px; flex: none; }
  .brand-name {
    font-family: "Didact Gothic", sans-serif;
    color: var(--ink); font-size: 34px; line-height: 1;
    white-space: nowrap;
  }
  .holder {
    position: absolute; left: 545px; width: 300px; top: 220px;
    text-align: center; font-family: "Didact Gothic", sans-serif; color: var(--orange);
  }
  .holder-name { font-size: 32px; line-height: 1.2; }
  .holder-role { font-size: 25px; margin-top: 12px; }

  .card-back {
    left: 115px; top: 618px; width: 888px; height: 514px;
    background: var(--back);
    font-family: "Cabin", sans-serif; color: var(--orange);
  }
  .phone-label { position: absolute; left: 20px; top: 18px; font-size: 26px; }
  .phone-number { position: absolute; right: 16px; top: 16px; font-size: 26px; letter-spacing: 0.5px; }
  .contact-line {
    position: absolute; left: 0; width: 100%; text-align: center; font-size: 26px;
  }
  .contact-email { top: 145px; }
  .contact-web { top: 237px; }
  .contact-address { top: 325px; }
  .divider {
    position: absolute; left: 168px; width: 553px; height: 1px;
  }
  .divider-orange { top: 205px; background: linear-gradient(to right, transparent, var(--orange) 15%, var(--orange) 85%, transparent); opacity: 0.6; }
  .divider-grey { top: 300px; background: linear-gradient(to right, transparent, #777 20%, var(--orange) 50%, #777 80%, transparent); opacity: 0.7; }
</style>
</head>
<body>
  <section class="card card-front">
    <div class="brand-panel">
      <svg class="brand-mark" viewBox="0 0 64 64" aria-hidden="true"><circle cx="32" cy="32" r="30" fill="var(--orange)"/></svg>
      <div class="brand-name">Kelvara North</div>
    </div>
    <div class="holder">
      <div class="holder-name">Dorian Welch</div>
      <div class="holder-role">Manager</div>
    </div>
  </section>

  <section class="card card-back">
    <div class="phone-label">Phone number</div>
    <div class="phone-number">123456789</div>
    <div class="contact-line contact-email">email@email.com</div>
    <div class="divider divider-orange"></div>
    <div class="contact-line contact-web">www.kelvaranorth.com.au</div>
    <div class="divider divider-grey"></div>
    <div class="contact-line contact-address">House no. 45, Reed Lane, Sydney, Australia</div>
  </section>
</body>
</html>
```